Wordpress Template Design using existing Logo and Colors

We are wanting a wordpress theme designing for our b2b marketing consultancy business. A comprehesive and elagant design to our current site www.pelvarogroup.com would be good.

Industry/Entity Type

Marketing

Font styles to use
Sans Serif

```html
<!DOCTYPE html>
<html lang="en">
<head>
<meta charset="utf-8">
<title>Pelvaro – B2B Data, Analytics and Marketing</title>
<link href="https://fonts.googleapis.com/css2?family=Michroma&family=Lato:wght@400;700;900&display=swap" rel="stylesheet">
<style>
:root{
  --red:#e3151d;
  --ink:#1f1f1f;
  --dark:#2d2d2d;
  --darker:#262626;
  --text:#333;
  --muted:#777;
  --white:#fff;
  --line:#e3151d;
}
*{margin:0;padding:0;box-sizing:border-box}
html,body{width:1200px;height:3727px;overflow:hidden}
body{position:relative;font-family:"Lato",Arial,sans-serif;color:var(--text);background:var(--white)}
.abs{position:absolute}
.display{font-family:"Michroma","Lato",sans-serif;text-transform:uppercase}
.btn{position:absolute;display:flex;align-items:center;justify-content:center;border-radius:5px;font:700 11px "Lato",sans-serif;letter-spacing:2.5px;text-transform:uppercase}
.btn-dark{background:var(--dark);color:var(--white)}
.btn-light{background:var(--white);color:var(--red)}

/* header */
.site-header{position:absolute;left:0;top:0;width:1200px;height:132px;background:#f4f4f4}
.brand{position:absolute;display:flex;align-items:center;gap:10px;font:900 40px "Lato",sans-serif;letter-spacing:1px}
.brand-mark{width:14px;height:14px;background:var(--red)}
.main-nav a{position:absolute;top:60px;font-size:15px;color:#333;text-decoration:none}
.main-nav a.active{color:var(--red)}
.main-nav a.active::after{content:"";position:absolute;left:0;right:0;top:29px;height:2px;background:var(--red)}
.caret{display:inline-block;width:0;height:0;border-left:4px solid transparent;border-right:4px solid transparent;border-top:5px solid #333;margin-left:3px;vertical-align:middle}

/* hero */
.hero{position:absolute;left:0;top:132px;width:1200px;height:626px;background:linear-gradient(180deg,#8c99a6 0%,#6f7b86 35%,#40464c 75%,#2a2d31 100%)}
.hero-title{position:absolute;left:0;width:1200px;top:262px;text-align:center;color:var(--white);font-size:31px;letter-spacing:1px}
.hero-sub{position:absolute;left:0;width:1200px;top:312px;text-align:center;color:var(--white);font-size:15px;line-height:21px}
.hero-arrow{position:absolute;top:268px}
.slider-dots span{position:absolute;top:781px;width:12px;height:12px;background:var(--ink)}
.slider-dots span.on{background:var(--red)}

/* section titles */
.sec-title{position:absolute;left:0;width:1200px;text-align:center;font-size:31px;color:var(--ink)}
.sec-title .hl{color:var(--red)}
.frame{position:absolute;border:3px solid var(--red);border-left:none;border-bottom:none}
.frame::after{content:"";position:absolute;right:-3px;bottom:-3px;width:100%;height:3px}

/* about */
.about-text{position:absolute;left:148px;width:904px;top:957px;text-align:center;font-size:14.5px;line-height:19px;color:#222}

/* services */
.services{position:absolute;left:0;top:1145px;width:1200px;height:527px;background:var(--dark)}
.services-photo{position:absolute;left:600px;top:0;width:600px;height:527px;background:linear-gradient(135deg,#dfe2e4 0%,#c9cdd0 45%,#a8adb1 100%)}
.services-heading{position:absolute;left:156px;top:120px;color:var(--white);font-size:31px;line-height:44px}
.services-heading .hl{color:var(--red)}
.services-text{position:absolute;left:156px;top:239px;width:300px;color:var(--white);font-size:14px;line-height:18px}
.service-card{position:absolute;left:529px;top:37px;width:552px;height:453px;background:var(--white)}
.service{position:absolute;width:170px;font-size:14px;line-height:18px;color:#222}
.service h3{font-size:14px;font-weight:400;letter-spacing:.3px;margin:14px 0 12px;text-transform:uppercase}
.service .more{display:block;margin-top:2px}
.service.featured{background:var(--red);color:var(--white);border-radius:4px;padding:14px 10px 0 12px;width:176px;height:169px}
.service.featured h3{margin-top:10px}

/* brochure */
.brochure-art{position:absolute;left:186px;top:1764px;width:219px;height:328px;background:linear-gradient(160deg,#f4f4f4 0%,#d8d8d8 40%,#555 70%,#1e1e1e 100%);box-shadow:8px 10px 16px rgba(0,0,0,.35);transform:rotate(-6deg)}
.brochure-title{position:absolute;left:623px;top:1836px;font-size:30px;color:var(--ink)}
.brochure-title .hl{color:var(--red)}
.brochure-text{position:absolute;left:603px;top:1911px;width:500px;text-align:center;font-size:14px;line-height:17px;font-weight:700;color:#222}

/* blogs */
.blogs{position:absolute;left:0;top:2181px;width:1200px;height:745px;background:radial-gradient(ellipse at 50% 55%,#5a5a5a 0%,#3b3b3b 55%,#2b2b2b 100%)}
.blogs .sec-title{color:var(--white)}
.blog-card{position:absolute;top:134px;width:301px;height:442px;background:var(--white)}
.blog-photo{height:219px;background:linear-gradient(180deg,#e9ecef 0%,#cfd3d6 55%,#b9b2ab 100%)}
.blog-photo.warm{background:linear-gradient(180deg,#2f2f2f 0%,#5a534a 50%,#7b6a55 100%)}
.blog-body{padding:18px 29px 0 29px;color:#222}
.blog-body h4{font:700 16px "Lato",sans-serif;letter-spacing:.5px}
.blog-meta{font-size:12px;line-height:17px;margin-top:5px}
.blog-body p{font-size:14px;line-height:17px;margin-top:14px}
.read-more{position:absolute;left:29px;top:405px;color:var(--red);font-size:11px;font-weight:700;letter-spacing:2px}
.blog-dots span{position:absolute;top:614px;width:12px;height:12px;background:var(--white)}
.blog-dots span.on{background:var(--red)}

/* contact */
.contact{position:absolute;left:0;top:2926px;width:1200px;height:457px;background:#fafafa}
.map-wash{position:absolute;left:150px;top:10px;width:900px;height:440px;background:radial-gradient(ellipse at 50% 50%,#ececec 0%,#f5f5f5 55%,#fafafa 80%)}
.field{position:absolute;left:425px;width:357px;height:26px;border-bottom:1px solid var(--red);color:var(--red);font-size:13px}

/* footer */
.site-footer{position:absolute;left:0;top:3383px;width:1200px;height:298px;background:var(--darker);color:var(--white)}
.foot-about{position:absolute;left:119px;top:119px;width:200px;font-size:13px;line-height:16px;font-weight:700}
.foot-col{position:absolute;top:52px}
.foot-col h5{font-family:"Michroma",sans-serif;font-weight:400;font-size:18px;text-transform:uppercase;letter-spacing:.5px;padding-bottom:8px;border-bottom:1px solid #999;display:inline-block}
.foot-col ul{list-style:none;margin-top:14px;font-size:13px}
.foot-col li{line-height:30px}
.contact-line{display:flex;gap:14px;font-size:13px;line-height:17px;margin-top:11px}
.contact-line svg{flex:none;margin-top:1px}
.copybar{position:absolute;left:0;top:3681px;width:1200px;height:46px;background:var(--red);color:var(--white)}
.copybar p{position:absolute;left:119px;top:15px;font-size:13px;font-weight:700}
.social{position:absolute;top:12px;width:20px;height:20px;border-radius:50%;background:var(--white)}
</style>
</head>
<body>

<header class="site-header">
  <div class="brand" style="left:124px;top:40px;color:var(--red)">PELVARO<span class="brand-mark"></span></div>
  <nav class="main-nav">
    <a href="#" class="active" style="left:458px">Home</a>
    <a href="#" style="left:534px">About Us</a>
    <a href="#" style="left:632px">Target Marketing<span class="caret"></span></a>
    <a href="#" style="left:785px">Data Managemet<span class="caret"></span></a>
    <a href="#" style="left:933px">Blogs</a>
    <a href="#" style="left:1008px">Contact Us</a>
  </nav>
</header>

<section class="hero" role="img" aria-label="City skyline of tall office towers under a cloudy sky">
  <svg class="hero-arrow" style="left:52px" width="24" height="32" viewBox="0 0 24 32"><path d="M18 3 L6 16 L18 29" stroke="#fff" stroke-width="5" fill="none"/></svg>
  <svg class="hero-arrow" style="left:1122px" width="24" height="32" viewBox="0 0 24 32"><path d="M6 3 L18 16 L6 29" stroke="#fff" stroke-width="5" fill="none"/></svg>
  <h1 class="hero-title display">Inbound &amp; Outbound Call Centers</h1>
  <p class="hero-sub">Attract new leads, increase sales &amp; inspire customers through<br>our in-country call centers network</p>
  <a class="btn btn-light" style="left:522px;top:375px;width:144px;height:37px">Read More</a>
</section>
<div class="slider-dots"><span class="on" style="left:570px"></span><span style="left:594px"></span><span style="left:618px"></span></div>

<section class="about">
  <h2 class="sec-title display" style="top:885px"><span class="hl">About</span> Us</h2>
  <div class="frame" style="left:633px;top:869px;width:66px;height:66px;border-bottom:3px solid var(--red)"></div>
  <p class="about-text">We are a B2B Data, Analytics and Marketing Consulting Company &nbsp;specialized in harnessing the power of potential data to strengthen connections between decisions makers, companies and products. We focus on solutions engineered to solve distinct challenges in the data, direct marketing, and analytics space.</p>
  <a class="btn btn-dark" style="left:532px;top:1051px;width:141px;height:42px">Read More</a>
</section>

<section class="services">
  <div class="services-photo" role="img" aria-label="Bright open-plan office with desks and glass partitions"></div>
  <h2 class="services-heading display"><span class="hl">Our</span><br>Services</h2>
  <div class="frame" style="left:300px;top:128px;width:58px;height:68px;border-bottom:3px solid var(--red)"></div>
  <p class="services-text">Learn our leading target marketing and intelligent data management solutions to attain new customers for your niche products and services.</p>
  <a class="btn btn-light" style="left:159px;top:338px;width:144px;height:40px">Read More</a>

  <div class="service-card">
    <div class="service" style="left:72px;top:57px">
      <svg width="34" height="32" viewBox="0 0 34 32" fill="none" stroke="#222" stroke-width="2"><rect x="2" y="12" width="14" height="18"/><rect x="18" y="4" width="14" height="26"/><path d="M6 17h6M6 22h6M22 10h6M22 15h6M22 20h6"/></svg>
      <h3>B2B Database</h3>
      Get access to Asia's leading market &amp; bus...
      <span class="more">Read More... »</span>
    </div>
    <div class="service" style="left:345px;top:57px">
      <svg width="32" height="32" viewBox="0 0 32 32" fill="none" stroke="#222" stroke-width="2.4"><path d="M5 20v-5a11 11 0 0 1 22 0v5"/><rect x="3" y="18" width="6" height="9" rx="2"/><rect x="23" y="18" width="6" height="9" rx="2"/><path d="M26 27q0 3-7 3"/></svg>
      <h3>Call Centre</h3>
      When your business requires instantan...
      <span class="more">Read More... »</span>
    </div>
    <div class="service featured" style="left:60px;top:229px">
      <svg width="34" height="34" viewBox="0 0 34 34" fill="none" stroke="#fff" stroke-width="2.4"><circle cx="17" cy="17" r="12"/><circle cx="17" cy="17" r="5"/><path d="M17 1v8M17 25v8M1 17h8M25 17h8"/></svg>
      <h3>Target Marketing</h3>
      We develop tailored marketing solutio...
      <span class="more">Read More... »</span>
    </div>
    <div class="service" style="left:345px;top:254px">
      <svg width="32" height="32" viewBox="0 0 32 32" fill="none" stroke="#222" stroke-width="2.4"><path d="M3 29h26"/><rect x="5" y="16" width="5" height="11"/><rect x="13.5" y="9" width="5" height="18"/><rect x="22" y="4" width="5" height="23"/></svg>
      <h3>Data Management</h3>
      We analyze your data and report on effec...
      <span class="more">Read More... »</span>
    </div>
  </div>
</section>

<section class="brochure">
  <div class="brochure-art" role="img" aria-label="Printed corporate brochure cover showing a dark glass office tower"></div>
  <h2 class="brochure-title display"><span class="hl">Corporate</span> Brochure</h2>
  <div class="frame" style="left:928px;top:1816px;width:146px;height:68px;border-bottom:3px solid var(--red)"></div>
  <p class="brochure-text">Learn our leading target marketing and intelligent data management solutions to attain new customers for your niche products and services.</p>
  <a class="btn btn-dark" style="left:785px;top:1972px;width:144px;height:40px">Download</a>
</section>

<section class="blogs" role="img" aria-label="Dim office interior in the background">
  <h2 class="sec-title display" style="top:54px"><span class="hl">Latest</span> Blogs</h2>
  <div class="frame" style="left:629px;top:38px;width:122px;height:66px;border-bottom:3px solid var(--red)"></div>

  <article class="blog-card" style="left:124px">
    <div class="blog-photo" role="img" aria-label="White office with red chairs and large windows"></div>
    <div class="blog-body"><h4>LOREM IPSUM</h4><div class="blog-meta">By &nbsp;DANIEL WARD<br>Feb.19.2018</div>
    <p>Lorem Ipsum is simply dummy text of the printing and typesetting industry. Lorem Ipsum has been the industry's standard dummy text.</p></div>
    <span class="read-more">READ MORE »</span>
  </article>
  <article class="blog-card" style="left:455px">
    <div class="blog-photo warm" role="img" aria-label="Meeting room with a long wooden table and black chairs"></div>
    <div class="blog-body"><h4>LOREM IPSUM</h4><div class="blog-meta">By &nbsp;DANIEL WARD<br>Feb.19.2018</div>
    <p>Lorem Ipsum is simply dummy text of the printing and typesetting industry. Lorem Ipsum has been the industry's standard dummy text.</p></div>
    <span class="read-more">READ MORE »</span>
  </article>
  <article class="blog-card" style="left:785px">
    <div class="blog-photo" role="img" aria-label="Open-plan white workspace with red office chairs"></div>
    <div class="blog-body"><h4>LOREM IPSUM</h4><div class="blog-meta">By &nbsp;DANIEL WARD<br>Feb.19.2018</div>
    <p>Lorem Ipsum is simply dummy text of the printing and typesetting industry. Lorem Ipsum has been the industry's standard dummy text.</p></div>
    <span class="read-more">READ MORE »</span>
  </article>

  <div class="blog-dots"><span class="on" style="left:570px"></span><span style="left:594px"></span><span style="left:618px"></span></div>
  <a class="btn btn-light" style="left:534px;top:658px;width:142px;height:40px">View More</a>
</section>

<section class="contact">
  <div class="map-wash" role="img" aria-label="Faint world map in the background"></div>
  <h2 class="sec-title display" style="top:93px"><span class="hl">Quick</span> Contact</h2>
  <div class="frame" style="left:676px;top:77px;width:78px;height:66px;border-bottom:3px solid var(--red)"></div>
  <div class="field" style="top:184px">Name</div>
  <div class="field" style="top:236px">E-mail</div>
  <div class="field" style="top:288px">Message</div>
  <a class="btn btn-dark" style="left:534px;top:368px;width:142px;height:36px">Submit</a>
</section>

<footer class="site-footer">
  <div class="brand" style="left:119px;top:52px;color:var(--white);font-size:34px">PELVARO<span class="brand-mark" style="width:12px;height:12px"></span></div>
  <p class="foot-about">Pelvaro is the primary source of market intelligence focused on identifying business oppo...</p>
  <p class="abs" style="left:119px;top:207px;font-size:13px;font-weight:700">Read More.... »</p>

  <div class="foot-col" style="left:395px">
    <h5>Quick Link</h5>
    <ul><li>Home</li><li>About Us</li><li>Target Marketing</li><li>Data Managemet</li><li>Blogs</li></ul>
  </div>

  <div class="foot-col" style="left:589px;width:230px">
    <h5>Global HQ</h5>
    <div class="contact-line" style="margin-top:16px"><svg width="14" height="14" viewBox="0 0 14 14"><path d="M3 1l3 3-2 2q2 4 4 4l2-2 3 3-2 2Q5 13 1 3z" fill="#fff"/></svg>+1 (555) 014-2290</div>
    <div class="contact-line"><svg width="14" height="14" viewBox="0 0 14 14"><rect x="1" y="3" width="12" height="9" fill="#fff"/><path d="M1 3l6 5 6-5" stroke="#262626" fill="none"/></svg>contactus.us@pelvarogroup.com</div>
    <div class="contact-line"><svg width="14" height="14" viewBox="0 0 14 14"><path d="M7 13s5-5 5-8a5 5 0 0 0-10 0c0 3 5 8 5 8z" fill="#fff"/><circle cx="7" cy="5" r="2" fill="#262626"/></svg>4410 Harbor Lane,<br>Suite 210, Oceanside,<br>CA 92054-1100, USA</div>
    <div class="contact-line"><svg width="14" height="14" viewBox="0 0 14 14" fill="none" stroke="#fff" stroke-width="2"><path d="M6 8l2-2M5 6L3 8a2 2 0 0 0 3 3l2-2M9 8l2-2a2 2 0 0 0-3-3L6 5"/></svg>www.pelvarogroup.com</div>
    <div class="contact-line"><svg width="14" height="14" viewBox="0 0 14 14" fill="none" stroke="#fff" stroke-width="1.6"><circle cx="7" cy="7" r="6"/><path d="M7 3v4h3"/></svg>Monday – Friday :<br>9AM – 6PM</div>
  </div>

  <div class="foot-col" style="left:847px;width:240px">
    <h5>Regional HQ</h5>
    <div class="contact-line" style="margin-top:16px"><svg width="14" height="14" viewBox="0 0 14 14"><path d="M3 1l3 3-2 2q2 4 4 4l2-2 3 3-2 2Q5 13 1 3z" fill="#fff"/></svg>+65 6100 2473</div>
    <div class="contact-line"><svg width="14" height="14" viewBox="0 0 14 14"><rect x="1" y="3" width="12" height="9" fill="#fff"/><path d="M1 3l6 5 6-5" stroke="#262626" fill="none"/></svg>contactus.sg@pelvarogroup.com</div>
    <div class="contact-line"><svg width="14" height="14" viewBox="0 0 14 14"><path d="M7 13s5-5 5-8a5 5 0 0 0-10 0c0 3 5 8 5 8z" fill="#fff"/><circle cx="7" cy="5" r="2" fill="#262626"/></svg>18 Kallang Way 2, #05-07 Meridian<br>Hub, Singapore 349731</div>
    <div class="contact-line"><svg width="14" height="14" viewBox="0 0 14 14" fill="none" stroke="#fff" stroke-width="2"><path d="M6 8l2-2M5 6L3 8a2 2 0 0 0 3 3l2-2M9 8l2-2a2 2 0 0 0-3-3L6 5"/></svg>www.pelvarogroup.com</div>
    <div class="contact-line"><svg width="14" height="14" viewBox="0 0 14 14" fill="none" stroke="#fff" stroke-width="1.6"><circle cx="7" cy="7" r="6"/><path d="M7 3v4h3"/></svg>Monday – Friday :<br>9AM – 6PM</div>
  </div>
</footer>

<div class="copybar">
  <p>Copyright © PELVARO 2018. All Right Reserved.</p>
  <span class="social" style="left:990px"></span>
  <span class="social" style="left:1016px"></span>
  <span class="social" style="left:1042px"></span>
  <span class="social" style="left:1068px"></span>
</div>

</body>
</html>
```